Letterhead Design for Higher Education provider

Company Name: PELV Credentials
Motto: Learning That Lasts
Address: Tamble House, Orchard Rise, Fenwick Trade Park, Dartford DA4 9LX, United Kingdom
T: +44 (0)20 7946 0382
E: info@pelv-example.org.uk
W: www.pelv-example.org.uk
Legal information: PELV Credentials is incorporated in England & Wales | Company Reg. No. 07315248

Target Market(s)

Higher Education provider

Industry/Entity Type

Education

Font styles to use
Sans Serif

Requirements
Must have
• Company Name, Address, tel, email, web, company legal information.
Nice to have
• motto
Should not have
• should not cover to much of printing areas

```html
<!DOCTYPE html>
<html lang="en">
<head>
<meta charset="utf-8">
<title>PELV Credentials – Letterhead</title>
<link rel="stylesheet" href="https://fonts.googleapis.com/css2?family=Open+Sans:wght@400;600;700&display=swap">
<style>
  :root {
    --brand-blue: #1b4f9c;
    --navy: #1a2f6b;
    --ink: #1d1d1f;
    --paper: #ffffff;
  }
  * { box-sizing: border-box; margin: 0; padding: 0; }
  html, body {
    width: 849px; height: 1200px; overflow: hidden;
    background: var(--paper);
    font-family: "Open Sans", Arial, sans-serif;
  }
  .letterhead {
    position: relative;
    width: 849px; height: 1200px;
    background: var(--paper);
  }
  .masthead {
    position: absolute; top: 26px; left: 0; right: 0;
    text-align: center;
  }
  .brand-name {
    display: inline-flex; align-items: center; gap: 8px;
    font-weight: 700; font-size: 30px; line-height: 1;
    color: var(--brand-blue);
  }
  .brand-mark {
    width: 10px; height: 10px; background: var(--brand-blue);
  }
  .motto {
    margin-top: 30px;
    font-weight: 600; font-size: 12.5px; line-height: 1;
    color: var(--ink);
  }
  .corner-arc {
    position: absolute; left: 0; bottom: 0;
  }
  .footer {
    position: absolute; left: 100px; right: 20px; bottom: 24px;
    text-align: center; font-size: 14.5px; line-height: 1;
    white-space: nowrap;
  }
  .footer-address { color: var(--ink); font-weight: 600; }
  .footer-contacts {
    margin-top: 11px; display: flex; justify-content: center; gap: 22px;
    color: var(--ink); font-weight: 600;
  }
  .contact-item { display: inline-flex; align-items: center; gap: 7px; }
  .contact-item svg { width: 15px; height: 15px; fill: var(--navy); }
  .footer-legal {
    margin-top: 6px; color: var(--brand-blue); font-weight: 600;
  }
</style>
</head>
<body>
<main class="letterhead">
  <header class="masthead">
    <div class="brand-name"><span class="brand-mark"></span>PELV Credentials</div>
    <p class="motto">Learning That Lasts</p>
  </header>

  <svg class="corner-arc" width="80" height="140" viewBox="0 0 80 140" aria-hidden="true">
    <circle cx="-60" cy="150" r="112" fill="none" stroke="var(--navy)" stroke-width="36"/>
  </svg>

  <footer class="footer">
    <p class="footer-address">Address: Tamble House, Orchard Rise, Fenwick Trade Park, Dartford DA4 9LX, United Kingdom</p>
    <div class="footer-contacts">
      <span class="contact-item">
        <svg viewBox="0 0 24 24" aria-hidden="true"><path d="M6.6 10.8a15.1 15.1 0 0 0 6.6 6.6l2.2-2.2a1 1 0 0 1 1-.25 11.4 11.4 0 0 0 3.6.57 1 1 0 0 1 1 1V20a1 1 0 0 1-1 1A17 17 0 0 1 3 4a1 1 0 0 1 1-1h3.5a1 1 0 0 1 1 1c0 1.25.2 2.45.57 3.57a1 1 0 0 1-.25 1z"/></svg>
        : +44 (0)20 7946 0382
      </span>
      <span class="contact-item">
        <svg viewBox="0 0 24 24" aria-hidden="true"><path d="M2 5h20v14H2z"/><path d="M3 6l9 7 9-7" fill="none" stroke="#fff" stroke-width="1.5"/></svg>
        info@pelv-example.org.uk
      </span>
      <span class="contact-item">
        <svg viewBox="0 0 24 24" aria-hidden="true"><circle cx="12" cy="12" r="10"/><path d="M2 12h20M12 2c3 3 3 17 0 20M12 2c-3 3-3 17 0 20" fill="none" stroke="#fff" stroke-width="1.3"/></svg>
        www.pelv-example.org.uk
      </span>
    </div>
    <p class="footer-legal">PELV Credentials is incorporated in England &amp; Wales | Company Reg. No. 07315248</p>
  </footer>
</main>
</body>
</html>
```